WordPress design needed for scientist

Hi! I am a female scientist (36 years old) in the field of marine science and biotechnology. I need a clean, engaging, modern WordPress website design. Not just a blog, but a site that shows pictures of my research and topics, can host PDFs of my research publications, and can have my Chirplinefeed (@miraleventhorp) and VidTrove videos embedded. Something a bit like this: http://www.quennimore.org.uk/ but with my content, and a more engaging design, like the template "PLUME"

My current webprofile from the University of Fjeldvik is here: http://www.uof.no/personer/Mira.Ruth.Leventhorp , but I need something that is more than this, that can inspire grant evaluators to pick me, and a website that shows the best sides of me and my research. I attach some representative pictures of me and my research that I would like to be used/incorporated in the webdesign.

Target Market(s)

other scientists, journalists, media, interested members of the public

Industry/Entity Type

Biotechnology

Font styles to use
Sans Serif

Requirements
Must have
• VidTrove video embedding of these videos:
• https://www.vidtrove.example/watch?v=Q7KPLMZTwe3
• https://www.vidtrove.example/watch?v=ht4bRcNpaXs
• https://www.vidtrove.example/watch?v=Ze9KUwdqYrB
• Slidora Presentations embedded: https://slidora.example/user/miraleventhorp/

```html
<!DOCTYPE html>
<html lang="en">
<head>
<meta charset="utf-8">
<title>Mira R. Leventhorp Ph.D</title>
<link href="https://fonts.googleapis.com/css2?family=Source+Sans+3:wght@400;600;700&display=swap" rel="stylesheet">
<style>
:root{
  --sky:#cfe6f8;
  --hero-bg:#ebebeb;
  --navy:#0b4a86;
  --title-blue:#0f4f8f;
  --tab:#efefef;
  --text-dark:#333;
  --text-grey:#555;
  --deep:#0d5796;
  --deep-2:#0a4a84;
  --foot-top:#2b92e2;
  --foot-bot:#1d7fd1;
  --white:#fff;
}
*{margin:0;padding:0;box-sizing:border-box}
html,body{width:880px;height:1200px;overflow:hidden}
body{position:relative;font-family:"Source Sans 3",Arial,sans-serif;background:var(--sky);color:var(--text-dark)}
.abs{position:absolute}

.topbar{left:0;top:0;width:880px;height:67px;background:var(--sky)}
.tab{top:32px;width:103px;height:35px;background:var(--tab);border-radius:4px 4px 0 0;
  font-size:10px;font-weight:600;letter-spacing:.3px;color:#444;display:flex;align-items:center;justify-content:center}
.tab.active{background:var(--navy);color:var(--white)}

.hero{left:0;top:67px;width:880px;height:307px;background:var(--hero-bg)}
.hero-name{left:105px;top:85px;color:var(--title-blue);line-height:1}
.hero-name .first{font-size:50px;font-weight:400;letter-spacing:.5px;display:block}
.hero-name .rest{font-size:31px;font-weight:400;display:block;margin-top:1px}
.tagline{left:105px;top:174px;font-size:14px;color:var(--text-grey)}
.dots{left:106px;top:277px;display:flex;gap:7px}
.dots span{width:7px;height:7px;border-radius:50%;background:var(--white)}
.dots span.on{background:var(--navy)}
.portrait{left:478px;top:0;width:316px;height:307px;
  background:radial-gradient(ellipse at 52% 48%,#d9a38a 0%,#b9805f 38%,#8a5a3c 62%,rgba(235,235,235,0) 74%)}

.videos{left:0;top:374px;width:880px;height:330px;
  background:linear-gradient(180deg,#a9d0f0 0%,#cfe6f6 28%,#8fc4ec 52%,#2a86d0 62%,#3d9be2 80%,#55aceb 100%)}
.sec-title{width:880px;left:0;text-align:center;font-size:21px;letter-spacing:.4px}
.videos .sec-title{top:34px;color:#243b55}
.rule{left:105px;width:670px;height:1px}
.videos .rule{top:72px;background:rgba(255,255,255,.55)}
.thumb{width:211px;height:131px;border:2px solid var(--white)}
.play{left:50%;top:50%;transform:translate(-50%,-50%)}
.vcap{font-size:10.5px;color:var(--white);line-height:16px;width:230px}
.vcap b{font-weight:700}
.btn-watch{width:82px;height:26px;border-radius:3px;background:linear-gradient(#0d5aa0,#073e74);
  box-shadow:0 2px 0 #052c55;color:var(--white);font-size:7.5px;font-weight:700;
  display:flex;align-items:center;justify-content:center;gap:5px}

.presentations{left:0;top:704px;width:880px;height:391px;background:linear-gradient(180deg,var(--deep) 0%,var(--deep-2) 100%)}
.presentations .sec-title{top:33px;color:var(--white)}
.presentations .rule{top:72px;background:rgba(255,255,255,.3)}
.arrow{top:42px}
.pimg{top:94px;width:211px;height:128px}
.phead{top:237px;font-size:10px;font-weight:700;color:var(--white);letter-spacing:.2px}
.ptext{top:257px;width:205px;font-size:7.5px;line-height:14px;color:#e4eef8}
.btn-more{top:319px;width:82px;height:25px;border-radius:3px;background:var(--white);color:#555;
  font-size:10px;display:flex;align-items:center;justify-content:center}

.footer{left:0;top:1095px;width:880px;height:105px;background:linear-gradient(180deg,var(--foot-top),var(--foot-bot))}
.foot-links{top:30px;left:0;width:880px;text-align:center;font-size:10.5px;color:var(--white);word-spacing:2px}
.foot-links span{margin:0 7px}
.copy{top:58px;left:0;width:880px;text-align:center;font-size:10px;color:var(--white)}
</style>
</head>
<body>

<header class="abs topbar">
  <nav>
    <div class="abs tab active" style="left:238px">PUBLICATIONS</div>
    <div class="abs tab" style="left:346px">BIO</div>
    <div class="abs tab" style="left:455px">PROJECT</div>
    <div class="abs tab" style="left:564px">VISION</div>
    <div class="abs tab" style="left:671px">CONTACT</div>
  </nav>
</header>

<section class="abs hero">
  <h1 class="abs hero-name"><span class="first">MIRA</span><span class="rest">R.LEVENTHORP PH.D</span></h1>
  <p class="abs tagline">Making Connections in Marine Science &amp; Society</p>
  <div class="abs dots"><span class="on"></span><span></span><span></span><span></span></div>
  <div class="abs portrait" role="img" aria-label="Portrait of the scientist smiling, curly hair, pink top"></div>
</section>

<section class="abs videos">
  <h2 class="abs sec-title" style="font-weight:400">LATEST VIDEOS</h2>
  <div class="abs rule"></div>

  <div class="abs thumb" style="left:105px;top:93px;background:linear-gradient(90deg,#7c8f2c 0%,#5e6e3a 35%,#9a9a96 70%,#c9c9c5 100%)" role="img" aria-label="Video still: scientist speaking at a lectern">
    <svg class="abs play" width="36" height="36" viewBox="0 0 36 36"><circle cx="18" cy="18" r="16" fill="rgba(0,0,0,.25)" stroke="#fff" stroke-width="3"/><path d="M14 10 L26 18 L14 26Z" fill="#fff"/></svg>
  </div>
  <div class="abs thumb" style="left:334px;top:93px;background:linear-gradient(180deg,#6fa7ee 0%,#79abef 62%,#2a0d0d 66%,#8a1a1a 100%)" role="img" aria-label="Video still: scientist giving a talk on stage">
    <svg class="abs play" width="36" height="36" viewBox="0 0 36 36"><circle cx="18" cy="18" r="16" fill="rgba(0,0,0,.25)" stroke="#fff" stroke-width="3"/><path d="M14 10 L26 18 L14 26Z" fill="#fff"/></svg>
  </div>
  <div class="abs thumb" style="left:563px;top:93px;background:linear-gradient(90deg,#6ea6d6 0%,#e07a2a 25%,#d67228 45%,#6f9a3a 70%,#cfd7df 100%)" role="img" aria-label="Video still: news interview beside a map of Scandinavia">
    <svg class="abs play" width="36" height="36" viewBox="0 0 36 36"><circle cx="18" cy="18" r="16" fill="rgba(0,0,0,.25)" stroke="#fff" stroke-width="3"/><path d="M14 10 L26 18 L14 26Z" fill="#fff"/></svg>
  </div>

  <p class="abs vcap" style="left:104px;top:234px"><b>Mira R. Leventhorp, PhD:</b><br>"How to save the ocean" | Talks at Lumenwork</p>
  <p class="abs vcap" style="left:334px;top:234px"><b>Mira R. Leventhorp, PhD:</b><br>"Fisheries management, how do we decide?"</p>
  <p class="abs vcap" style="left:563px;top:234px"><b>Mira R. Leventhorp, PhD:</b><br>Meridian News Oct 8, 2015</p>

  <div class="abs btn-watch" style="left:105px;top:274px"><svg width="8" height="8" viewBox="0 0 8 8"><circle cx="4" cy="4" r="4" fill="#fff"/><path d="M3 2 L6 4 L3 6Z" fill="#0a4a86"/></svg>WATCH NOW</div>
  <div class="abs btn-watch" style="left:334px;top:274px"><svg width="8" height="8" viewBox="0 0 8 8"><circle cx="4" cy="4" r="4" fill="#fff"/><path d="M3 2 L6 4 L3 6Z" fill="#0a4a86"/></svg>WATCH NOW</div>
  <div class="abs btn-watch" style="left:563px;top:274px"><svg width="8" height="8" viewBox="0 0 8 8"><circle cx="4" cy="4" r="4" fill="#fff"/><path d="M3 2 L6 4 L3 6Z" fill="#0a4a86"/></svg>WATCH NOW</div>
</section>

<section class="abs presentations">
  <svg class="abs arrow" style="left:104px" width="8" height="12" viewBox="0 0 8 12"><path d="M6 1 L2 6 L6 11" fill="none" stroke="#9cc0e2" stroke-width="1.5"/></svg>
  <svg class="abs arrow" style="left:768px" width="8" height="12" viewBox="0 0 8 12"><path d="M2 1 L6 6 L2 11" fill="none" stroke="#9cc0e2" stroke-width="1.5"/></svg>
  <h2 class="abs sec-title" style="font-weight:400">LATEST PRESENTATIONS</h2>
  <div class="abs rule"></div>

  <div class="abs pimg" style="left:105px;background:linear-gradient(135deg,#2f63c9 0%,#3f7ee0 45%,#1d4fa6 100%)" role="img" aria-label="Scientist presenting in front of a projected research vessel"></div>
  <div class="abs pimg" style="left:334px;background:linear-gradient(135deg,#8a6a45 0%,#4a3a2c 50%,#2a2420 100%)" role="img" aria-label="Workshop participants working at laptops around a table"></div>
  <div class="abs pimg" style="left:563px;background:linear-gradient(180deg,#8a8c90 0%,#b9b6ae 55%,#d8cfc0 100%)" role="img" aria-label="Group discussion around a meeting table"></div>

  <h3 class="abs phead" style="left:103px">PRESENTATION1</h3>
  <h3 class="abs phead" style="left:333px">PRESENTATION 2</h3>
  <h3 class="abs phead" style="left:563px">PRESENTATION 3</h3>

  <p class="abs ptext" style="left:104px">Lorem Ipsum is simply dummy text of the printing and typesetting industry. Lorem Ipsum has been the industry's standard dummy text ever since the 1500s.</p>
  <p class="abs ptext" style="left:333px">Lorem Ipsum is simply dummy text of the printing and typesetting industry. Lorem Ipsum has been the industry's standard dummy text ever since the 1500s.</p>
  <p class="abs ptext" style="left:563px">Lorem Ipsum is simply dummy text of the printing and typesetting industry. Lorem Ipsum has been the industry's standard dummy text ever since the 1500s.</p>

  <div class="abs btn-more" style="left:105px">MORE INFO</div>
  <div class="abs btn-more" style="left:334px">MORE INFO</div>
  <div class="abs btn-more" style="left:563px">MORE INFO</div>
</section>

<footer class="abs footer">
  <p class="abs foot-links">PUBLICATION<span>|</span>BIO<span>|</span>PROJECT<span>|</span>VISION<span>|</span>CONTACT US</p>
  <p class="abs copy">© 2016 COMPANY NAME &nbsp;| ALL RIGHTS RESERVED</p>
</footer>

</body>
</html>
```